Northbrook Velvet Coil Supply needs a packaging design

We need a packaging design for a new hair extension company based in Edmonton, Alberta called Solvane Co. Our packaging should communicate high quality, luxurious hair that will never tangle or dry out. The product will be marketed to salon professionals as well as clients. There must be an opening to see the hair from the outside.

Our advertising campaign is going to be based on boho chic; Dorian Kessley/ Amber Thistle/Copper Lantern.

Target Market(s)

Women and beauty industry professionals. High end market.

Industry/Entity Type

Advertising

Requirements
Must have
• "Highest quality 100% Remi hair!" should be written on the front of the package. In addition, we would like to add text to the back or inside of the packaging as follows:
• Hair Collection and Color Processing:
• Only the highest quality hair is selected which ensures high moisture and nutrient content
• The hair is directly cut from the donor which ensures that the hair cuticle remains intact and always tangle-free
• No chemicals are used in dyeing the hair
• The hair will never fade due to the mild and healthy herbal extract used in the dyeing process which gently penetrates to the inner core of the hair
• Care Instructions:
• Solvane Co provides only the highest in quality Remi hair that demands very little care to maintain it’s luxurious feel.
• Use a proper extension bristle brush
• Wash the hair with a sulfate-free shampoo and follow with a moisturizing conditioner that is formulated for hair extensions
• Do not apply any type of chemicals to the hair
• We proudly show our immense passion for delivering superior quality in our full product line.
• We insist that it is important for you to know and understand what you are purchasing in your hair extensions. We guarantee the highest quality of our products.
• Solvane Co is strongly committed to serving their clients with utmost integrity, believing in a foundation of personal and professional ethics and our 20 years service in the beauty industry.

```html
<!DOCTYPE html>
<html lang="en">
<head>
<meta charset="utf-8">
<title>Solvane Co – Hair Extension Package Front</title>
<link rel="stylesheet" href="https://fonts.googleapis.com/css2?family=Cormorant+SC:wght@500&display=swap">
<style>
  :root {
    --page-bg: #ffffff;
    --pack-black: #0d0b09;
    --lattice-tone: #1a150e;
    --gold: #c9a13a;
    --gold-deep: #9a7526;
    --ivory: #f7f3ea;
    --hair-dark: #2a2325;
    --hair-mid: #4a4043;
    --hair-light: #5d5356;
  }
  html, body {
    margin: 0;
    padding: 0;
    width: 927px;
    height: 1200px;
    overflow: hidden;
    background: var(--page-bg);
  }
  .canvas {
    position: relative;
    width: 927px;
    height: 1200px;
  }
  .package-front {
    position: absolute;
    left: 281px;
    top: 100px;
    width: 378px;
    height: 1010px;
    background: radial-gradient(ellipse at 50% 45%, var(--lattice-tone) 0%, var(--pack-black) 75%);
  }
  .brand-plate {
    position: absolute;
    left: 74px;
    top: 58px;
    width: 270px;
    height: 165px;
    box-sizing: border-box;
    border: 1.5px solid var(--gold);
    background: var(--pack-black);
    display: flex;
    flex-direction: column;
    align-items: center;
    justify-content: center;
    gap: 14px;
  }
  .brand-dot {
    width: 34px;
    height: 34px;
    border-radius: 50%;
    background: var(--gold);
  }
  .brand-name {
    margin: 0;
    font-family: "Cormorant SC", "Times New Roman", serif;
    font-weight: 500;
    font-size: 40px;
    line-height: 1;
    letter-spacing: 1px;
    color: var(--ivory);
  }
  .hair-window {
    position: absolute;
    left: 145px;
    top: 252px;
    width: 125px;
    height: 553px;
    box-sizing: border-box;
    border: 1.5px solid var(--gold-deep);
    background: linear-gradient(90deg, var(--hair-dark) 0%, var(--hair-mid) 35%, var(--hair-light) 55%, var(--hair-mid) 75%, var(--hair-dark) 100%);
  }
  .front-claim {
    position: absolute;
    left: 0;
    right: 0;
    top: 966px;
    margin: 0;
    text-align: center;
    font-family: "Cormorant SC", "Times New Roman", serif;
    font-weight: 500;
    font-size: 19px;
    letter-spacing: 0.5px;
    color: var(--ivory);
  }
</style>
</head>
<body>
  <main class="canvas">
    <section class="package-front">
      <div class="brand-plate">
        <span class="brand-dot" aria-hidden="true"></span>
        <p class="brand-name">Solvane Co</p>
      </div>
      <div class="hair-window" role="img" aria-label="Window showing a straight dark brown hair extension weft"></div>
      <p class="front-claim">Highest Quality 100% Remi Hair!</p>
    </section>
  </main>
</body>
</html>
```